2 Funky Pages + EASY stock logo = Construction Website

We would like a funky new website - Just 2 pages - to promote our project management company. A logo is also needed, but we'll provide a stock image which just needs a colour change a text added.

Here are the instructions:

"Hollow Fern Builders"

#logo
The one I'd like is attached. Please change font and positioning of text though.

Tagline is "Don't be normal - Be clever"

#Colour combo
756897 Wood Veneer
D5D6D2 sand dollar
353C3F charcoal
962715 brick red

#Home - Page 1

Our cost-price home build service will save you thousands.
No, seriously - Here's how we do it (button)

- Pay what the home building companies do.
- HFB will manage the entire project.
- Use Stonequay Guaranteed builders and materials.
- Tender for the best industry rates.
- Get a full budget calculated for the build.
- Avoid inflated 'Fixed-price' builds.
See how it works (button)

Contact Us: 0800 617 280
enquire - Name, Phone, email, comment - SEND

#How it works - Page 2

Traditional fixed price contracts are popular because it means that any risk of unexpected problems is carried by the home builder, but the builder will generally load the price about 10 times above the actual risk carried.

It's like an over-priced insurance policy, on steroids.

Clever people do things differently.

Here's how a cost-price build works...

1) Tell us what you want to build. Dream home, townhouse, investment property, whatever.

2) We'll put a design together for you, or you can choose from a bunch of plans we've already got.

3) We'll give you a conservative price estimate.

4) We finish tweaking your plans, then send them out to our network of more than 200 builders, subcontractors and tradesmen.

5) We collect the quotes, pick the best prices, and finalise your budget. Now you buy us beer, cause you've finally realised how much you're saving.

6) Tell your friends how awesome we are, while we lodge your building consent application with Council.

7) We coordinate the builders and subbies (look, you're already speaking trade-talk) from start to finish. You pay the cost price on their work each month.

We're happy to talk numbers and give you an estimate.

Contact Us: 0800 617 280

Reason: I have seen some great design elements, but need them to come together in one site design. Also, there appears to be less attention paid to the second page design ('how it works') than is necessary... There is no viable contender there yet, compared with the great home page submissions. I've also added some further info to the brief, and note that many submissions have ignored the colour combo I've requested.

Industry/Entity Type

Construction

Number of Pages Required

2 page

Requirements
Must have
• Stonequayer logo (small)
• Colour combo described in brief.
Nice to have
• I've attached a stock image I like, but it's certainly not essential. I do like images with clear backgrounds though - they tend to produce a crisp looking site.
• There is a wider image similar to this, available on Vorlin Imagery, but Pitchwell Hub won't let me attach it.
Should not have
• Photos of cheesy American faces.

```html
<!DOCTYPE html>
<html lang="en">
<head>
<meta charset="utf-8">
<title>Hollow Fern Builders</title>
<link href="https://fonts.googleapis.com/css2?family=Montserrat:wght@400;500;600;700;800&family=Open+Sans:wght@400;600;700&display=swap" rel="stylesheet">
<style>
:root{
  --charcoal:#353c3f;
  --veneer:#756897;
  --veneer-soft:rgba(117,104,151,.82);
  --sand:#d5d6d2;
  --lime:#b5d334;
  --ink:#2e3336;
  --muted:#666a6d;
  --white:#ffffff;
}
*{box-sizing:border-box;margin:0;padding:0}
html,body{width:777px;height:1200px;overflow:hidden}
body{position:relative;background:var(--white);font-family:"Open Sans",sans-serif;color:var(--ink)}
.abs{position:absolute}
.center{left:0;width:777px;text-align:center}

.header{position:absolute;left:0;top:0;width:777px;height:58px;background:var(--charcoal);z-index:3}
.brand{position:absolute;left:52px;top:-20px;width:120px;height:120px;border-radius:50%;background:var(--charcoal);z-index:4;display:flex;align-items:flex-end;justify-content:center;padding-bottom:26px}
.brand-name{font-family:"Montserrat",sans-serif;font-weight:600;font-size:10px;color:var(--white);text-align:center;line-height:1.3}
.brand-mark{position:absolute;left:50px;top:32px;width:20px;height:20px;border:2px solid var(--lime)}
.topline{position:absolute;top:10px;right:63px;display:flex;align-items:center;gap:6px;z-index:5;color:var(--white);font-family:"Montserrat",sans-serif;font-size:9.5px}
.social{width:20px;height:20px;border:1.5px solid var(--white);border-radius:50%}
.contact-item{display:flex;align-items:center;gap:6px;margin-left:8px}
.contact-icon{width:20px;height:20px;border:1.5px solid var(--white);border-radius:50%;display:flex;align-items:center;justify-content:center}
.nav{position:absolute;top:42px;left:0;width:777px;height:12px;z-index:5;font-family:"Montserrat",sans-serif;font-weight:500;font-size:8.5px;color:var(--white)}
.nav span{position:absolute;top:0}
.nav .active{color:#a99be0}

.hero{position:absolute;left:0;top:58px;width:777px;height:297px;background:linear-gradient(180deg,#8a7357 0%,#b59a73 22%,#9d968c 50%,#a7a59f 72%,#8b8781 100%)}
.hero-title{top:163px;font-family:"Montserrat",sans-serif;font-weight:800;font-size:33px;color:var(--white);letter-spacing:-.3px;text-shadow:0 1px 3px rgba(0,0,0,.35)}
.hero-sub{top:202px;font-size:14.5px;color:var(--white);text-shadow:0 1px 3px rgba(0,0,0,.4)}
.btn{position:absolute;background:var(--veneer);color:var(--white);font-family:"Montserrat",sans-serif;font-weight:700;display:flex;align-items:center;justify-content:center;letter-spacing:.3px}
.hero-btn{left:312px;top:234px;width:153px;height:32px;font-size:10px}
.dots{position:absolute;top:312px;left:365px;display:flex;gap:2px}
.dots i{width:11px;height:11px;border:1.5px solid var(--white);border-radius:50%}
.dots i.on{background:var(--veneer)}

.badge-circle{position:absolute;width:48px;height:48px;border-radius:50%;background:var(--white)}

.section-title{font-family:"Montserrat",sans-serif;font-weight:600;font-size:16px;color:var(--ink)}
.intro{font-size:7.4px;line-height:15px;color:var(--muted)}

.feature{position:absolute;top:477px;width:112px;text-align:center}
.feature-icon{width:58px;height:58px;margin:0 auto;border:2px solid var(--veneer);border-radius:50%;display:flex;align-items:center;justify-content:center}
.feature-text{margin-top:12px;font-size:8.8px;line-height:12px;color:#4a4e51}
.how-btn{left:306px;top:604px;width:165px;height:31px;font-size:10px}

.quote-band{position:absolute;left:0;top:681px;width:777px;height:179px;background:linear-gradient(135deg,#8f83ae 0%,#a49bbd 45%,#8b80a8 100%)}
.band-title{top:725px;font-family:"Montserrat",sans-serif;font-weight:600;font-size:16px;color:var(--white)}
.band-text{top:749px;font-size:7.4px;line-height:15px;color:var(--white)}
.outline-btn{position:absolute;left:228px;top:797px;width:104px;height:28px;border:2px solid var(--white);color:var(--white);font-family:"Montserrat",sans-serif;font-weight:600;font-size:9.5px;display:flex;align-items:center;justify-content:center}
.call{position:absolute;left:345px;top:801px;display:flex;align-items:center;gap:8px;color:var(--white);font-family:"Montserrat",sans-serif;font-size:9.5px;font-weight:500}
.call strong{font-size:15.5px;font-weight:700;margin-left:2px}

.enquiry{position:absolute;left:111px;top:902px;width:555px;height:200px;border:1px solid #dcdcdc}
.enquiry-title{position:absolute;left:198px;top:-9px;padding:0 18px;background:var(--white);font-family:"Montserrat",sans-serif;font-weight:600;font-size:15.5px;color:var(--ink)}
.label{position:absolute;font-size:7px;color:#55595c;letter-spacing:.2px}
.field{position:absolute;border:1px solid #cfcfcf;background:var(--white)}
.submit{left:345px;top:1051px;width:87px;height:27px;font-size:9.5px}

.footer{position:absolute;left:0;top:1139px;width:777px;height:61px;background:var(--charcoal);color:var(--white)}
.footer-links{position:absolute;left:64px;top:18px;font-size:7.6px}
.footer-links span{margin:0 3px}
.copyright{position:absolute;left:64px;top:34px;font-size:7.2px}
.partner{position:absolute;left:674px;top:5px;width:40px;height:50px;background:#1f3f8f}
</style>
</head>
<body>

<header class="header"></header>
<div class="brand">
  <div class="brand-mark"></div>
  <div class="brand-name">Hollow Fern<br>Builders</div>
</div>
<div class="topline">
  <div class="social"></div><div class="social"></div><div class="social"></div>
  <div class="contact-item">
    <div class="contact-icon"><svg width="10" height="10" viewBox="0 0 24 24"><path fill="#fff" d="M6.6 10.8a15 15 0 0 0 6.6 6.6l2.2-2.2c.3-.3.7-.4 1-.2 1.1.4 2.3.6 3.6.6.6 0 1 .4 1 1V20c0 .6-.4 1-1 1A17 17 0 0 1 3 4c0-.6.4-1 1-1h3.5c.6 0 1 .4 1 1 0 1.3.2 2.5.6 3.6.1.3 0 .7-.2 1z"/></svg></div>
    <span>0800 617 280</span>
  </div>
  <div class="contact-item">
    <div class="contact-icon"><svg width="10" height="8" viewBox="0 0 20 14"><rect x="1" y="1" width="18" height="12" rx="1" fill="#fff"/><path d="M1 1l9 7 9-7" stroke="#353c3f" stroke-width="1.6" fill="none"/></svg></div>
    <span>info@hollowfernbuilders.example</span>
  </div>
</div>
<nav class="nav">
  <span class="active" style="left:311px">HOME</span>
  <span style="left:360px">ABOUT US</span>
  <span style="left:426px">HOW IT WORKS</span>
  <span style="left:514px">PROJECTS</span>
  <span style="left:580px">NEWS</span>
  <span style="left:630px">CONTACT US</span>
  <span style="left:706px;top:-1px"><svg width="9" height="9" viewBox="0 0 12 12"><circle cx="5" cy="5" r="3.6" stroke="#fff" stroke-width="1.6" fill="none"/><path d="M7.7 7.7l3 3" stroke="#fff" stroke-width="1.8"/></svg></span>
</nav>

<section class="hero" role="img" aria-label="Photo of a house under construction with timber roof trusses over block walls"></section>
<h1 class="abs center hero-title">DON'T BE NORMAL - BE CLEVER</h1>
<p class="abs center hero-sub">Our cost-price home build service will save you thousands. No, seriously</p>
<div class="btn hero-btn">HOW WE DO IT &nbsp;&gt;&gt;</div>
<div class="dots"><i class="on"></i><i></i><i></i><i></i></div>

<div class="badge-circle" style="left:365px;top:331px"></div>

<h2 class="abs center section-title" style="top:396px">WELCOME TO HOLLOW FERN BUILDERS</h2>
<p class="abs center intro" style="top:426px">Traditional fixed price contracts are popular because it means that any risk of unexpected problems is carried by the home builder,<br>but the builder willgenerally load the price about 10 times above the actual risk carried.</p>

<div class="feature" style="left:56px">
  <div class="feature-icon"><svg width="34" height="26" viewBox="0 0 34 26"><rect x="6" y="2" width="26" height="17" rx="2" fill="none" stroke="#756897" stroke-width="2.4"/><rect x="6" y="6" width="26" height="3" fill="#756897"/><rect x="22" y="11" width="7" height="4" rx="2" fill="#756897"/><circle cx="9" cy="18" r="7" fill="#756897"/><path d="M5.5 18l2.5 2.5 4.5-5" stroke="#fff" stroke-width="2" fill="none"/></svg></div>
  <p class="feature-text">Pay what the home<br>building companies do.</p>
</div>
<div class="feature" style="left:168px">
  <div class="feature-icon"><svg width="32" height="30" viewBox="0 0 32 30"><circle cx="12" cy="16" r="7" fill="none" stroke="#756897" stroke-width="5" stroke-dasharray="3 2.5"/><circle cx="12" cy="16" r="4.5" fill="#756897"/><circle cx="12" cy="16" r="2" fill="#fff"/><circle cx="25" cy="8" r="4" fill="none" stroke="#756897" stroke-width="3.5" stroke-dasharray="2 1.8"/><circle cx="25" cy="22" r="3.5" fill="none" stroke="#756897" stroke-width="3" stroke-dasharray="2 1.6"/></svg></div>
  <p class="feature-text">HFB will manage the<br>entire project.</p>
</div>
<div class="feature" style="left:280px">
  <div class="feature-icon"><svg width="28" height="28" viewBox="0 0 28 28"><rect x="2" y="12" width="6" height="13" rx="1" fill="#756897"/><path d="M10 13l5-9c2-1 3.5.5 3 3l-1 5h6c2 0 3 1.5 2.5 3l-2.5 8c-.5 1.5-1.5 2-3 2H10z" fill="#756897"/></svg></div>
  <p class="feature-text">Use Stonequay<br>Guaranteed builders<br>&amp; materials.</p>
</div>
<div class="feature" style="left:392px">
  <div class="feature-icon"><svg width="30" height="26" viewBox="0 0 30 26"><path d="M2 2v22h26" fill="none" stroke="#756897" stroke-width="2"/><rect x="6" y="12" width="3.5" height="10" fill="#756897"/><rect x="11.5" y="7" width="3.5" height="15" fill="#756897"/><rect x="17" y="14" width="3.5" height="8" fill="#756897"/><rect x="22.5" y="9" width="3.5" height="13" fill="#756897"/></svg></div>
  <p class="feature-text">Tender for the best<br>industry rates.</p>
</div>
<div class="feature" style="left:504px">
  <div class="feature-icon"><svg width="24" height="30" viewBox="0 0 24 30"><rect x="1.5" y="1.5" width="21" height="27" rx="2" fill="none" stroke="#756897" stroke-width="2.4"/><rect x="5" y="5" width="14" height="5" fill="#756897"/><g fill="#756897"><rect x="5" y="13" width="3.5" height="3"/><rect x="10.3" y="13" width="3.5" height="3"/><rect x="15.5" y="13" width="3.5" height="3"/><rect x="5" y="18" width="3.5" height="3"/><rect x="10.3" y="18" width="3.5" height="3"/><rect x="15.5" y="18" width="3.5" height="3"/><rect x="5" y="23" width="3.5" height="3"/><rect x="10.3" y="23" width="3.5" height="3"/><rect x="15.5" y="23" width="3.5" height="3"/></g></svg></div>
  <p class="feature-text">Get a full budget<br>calculated for the build.</p>
</div>
<div class="feature" style="left:616px">
  <div class="feature-icon"><svg width="28" height="28" viewBox="0 0 28 28"><path d="M3 4c0-.6.4-1 1-1h9l12 12c.6.6.6 1.4 0 2l-8 8c-.6.6-1.4.6-2 0L3 13z" fill="#756897"/><circle cx="9" cy="9" r="2.2" fill="#fff"/></svg></div>
  <p class="feature-text">Avoid inflated<br>“Fixed-price” builds.</p>
</div>

<div class="btn how-btn">SEE HOW IT WORKS</div>

<section class="quote-band" role="img" aria-label="Photo of house floor plans with a pencil and nails, tinted in lavender"></section>
<div class="badge-circle" style="left:365px;top:658px"></div>
<h2 class="abs center band-title">WE'RE HAPPY TO TALK NUMBERS AND GIVE YOU AN ESTIMATE</h2>
<p class="abs center band-text">At vero eos et accusamus et iusto odio dignissimos ducimus qui blanditiis praesentium voluptatum deleniti atque corrupti<br>quos dolores et quas molestias excepturi sint occaecati cupiditate non provident</p>
<div class="outline-btn">CONATCT US</div>
<div class="call"><span>OR</span><span>CALL US ON &nbsp;:</span><strong>0800 617 280</strong></div>

<section class="enquiry">
  <h2 class="enquiry-title">ENQUIRY FORM</h2>
</section>
<span class="label" style="left:153px;top:932px">NAME :</span>
<span class="label" style="left:311px;top:932px">PHONE :</span>
<span class="label" style="left:469px;top:932px">EMAIL :</span>
<div class="field" style="left:153px;top:948px;width:154px;height:23px"></div>
<div class="field" style="left:311px;top:948px;width:154px;height:23px"></div>
<div class="field" style="left:469px;top:948px;width:155px;height:23px"></div>
<span class="label" style="left:153px;top:980px">COMMENT :</span>
<div class="field" style="left:153px;top:994px;width:471px;height:44px"></div>
<div class="btn submit">SUBMIT</div>

<footer class="footer">
  <div class="footer-links">Home<span>|</span>About us<span>|</span>How It Works<span>|</span>Projects<span>|</span>News<span>|</span>Contact Us</div>
  <div class="copyright">© 2016, Hollow Fern Builders. All Rights Reserved.</div>
  <div class="partner"></div>
</footer>

</body>
</html>
```